Business card design needed

Our company background is that we provides transfers to and from the airport, social & corporate events, weddings.
We are also available for charter for birthday party, wine tastings, concerts, anniversary, school balls etc.
Our business cards have to reflect that we have a professional company, they are our first contact and have to stand out from the other 'players' in the market.

Industry/Entity Type

School

Contact Information for Business Card

VESTAR PTH, Teodor & Marguerite, mob: 0427 381 592, PO Box 284, Brenton WA 6158, ABN 52 614 203 178, Lic 7169/2058,

Requirements
Must have
• Telephone number: 0427 381 592
Website: www.VESTARPTH.com.au
postal address: PO Box 284, Brenton WA 6158
Licences: Lic 7169/2058

***If using the new photo (one with the bus and buildings behind it), if possible can the buildings be cropped out. Thanks
Nice to have
• would be nice to have the pics of the vehicle(s), preferred the Vel on the card but not too fussed.
Should not have
• Picture of vehicle we don't have in our fleet. (We ONLY have the Velarions and Murako Densa mini bus)

```html
<!DOCTYPE html>
<html lang="en">
<head>
<meta charset="utf-8">
<title>VESTAR PTH – Business Card</title>
<link rel="stylesheet" href="https://fonts.googleapis.com/css2?family=Cinzel:wght@400;600&display=swap">
<style>
  :root {
    --page-bg: #e6e8ea;
    --card-white: #ffffff;
    --ink: #1c1a1a;
    --band-dark: #221f20;
    --band-text: #ffffff;
    --swoosh-grey: #9a9a9c;
    --swoosh-light: #d2d2d4;
    --photo-sky: #d7e4ec;
    --photo-trees: #5f7a55;
    --photo-car: #bdb6a6;
    --photo-paving: #a3654f;
  }
  html, body {
    margin: 0;
    width: 1200px;
    height: 975px;
    overflow: hidden;
    background: var(--page-bg);
  }
  .business-card {
    position: absolute;
    left: 75px;
    top: 187px;
    width: 1050px;
    height: 600px;
    background: var(--card-white);
    box-shadow: 0 10px 30px rgba(0,0,0,0.18);
    overflow: hidden;
    font-family: "Cinzel", "Times New Roman", serif;
    color: var(--ink);
  }
  .card-shapes {
    position: absolute;
    inset: 0;
    width: 1050px;
    height: 600px;
  }
  .brand-name {
    position: absolute;
    left: 40px;
    top: 58px;
    margin: 0;
    font-size: 58px;
    font-weight: 400;
    letter-spacing: 1px;
    line-height: 1;
    color: var(--ink);
  }
  .owner-names {
    position: absolute;
    left: 42px;
    top: 210px;
    margin: 0;
    font-size: 27px;
    font-weight: 400;
    letter-spacing: 1.5px;
  }
  .contact-list {
    position: absolute;
    left: 42px;
    top: 328px;
    margin: 0;
    padding: 0;
    list-style: none;
    font-size: 22px;
    line-height: 45px;
    letter-spacing: 0.5px;
  }
  .website {
    position: absolute;
    left: 42px;
    top: 545px;
    margin: 0;
    font-size: 25px;
    letter-spacing: 1.5px;
    color: var(--band-text);
  }
</style>
</head>
<body>
  <div class="business-card">
    <svg class="card-shapes" viewBox="0 0 1050 600">
      <defs>
        <linearGradient id="photoTones" x1="0" y1="0" x2="0" y2="1">
          <stop offset="0" stop-color="var(--photo-sky)"/>
          <stop offset="0.3" stop-color="var(--photo-trees)"/>
          <stop offset="0.55" stop-color="var(--photo-car)"/>
          <stop offset="0.75" stop-color="var(--photo-car)"/>
          <stop offset="1" stop-color="var(--photo-paving)"/>
        </linearGradient>
        <linearGradient id="swooshTone" x1="0" y1="0" x2="0" y2="1">
          <stop offset="0" stop-color="var(--swoosh-light)"/>
          <stop offset="0.5" stop-color="var(--swoosh-grey)"/>
          <stop offset="1" stop-color="var(--swoosh-light)"/>
        </linearGradient>
      </defs>
      <path class="vehicle-photo" role="img" aria-label="Photograph of the company's silver Velarion luxury sedan parked on brick paving with trees behind"
            d="M610 0 H1050 V600 H600 C545 430 545 160 610 0 Z" fill="url(#photoTones)"/>
      <path class="card-swoosh" d="M585 0 H625 C560 150 560 430 612 600 H575 C515 430 520 150 585 0 Z" fill="url(#swooshTone)"/>
      <rect class="footer-band" x="0" y="515" width="590" height="85" fill="var(--band-dark)"/>
    </svg>

    <h1 class="brand-name">VESTAR PTH</h1>
    <p class="owner-names">Teodor &amp; Marguerite</p>
    <ul class="contact-list">
      <li class="postal-address">PO Box 284, Brenton WA 6158</li>
      <li class="phone">Tel: 0427 381 592</li>
      <li class="licence">Lic 7169/2058 | ABN 52 614 203 178</li>
    </ul>
    <p class="website">WWW.VESTARPTH.COM.AU</p>
  </div>
</body>
</html>
```